Tranquil Pathway Business Card

Logo attached. (will be printing onto thick white/off white textured card)

Double sided business card for two Therapists working at Tranquil Pathway.

Require one design, but with different name and mobile numbers on each card.

Target Market(s)

Medical, Health

Industry/Entity Type

Business

Contact Information for Business Card

Need one business card design, but a separate card for each person - Colin Marchetti and Marieke de Boeckx.

FRONT OF CARD

Logo

Name (Colin Marchetti on one card, Marieke de Boeckx on the other)
Professional Clinical Hypnotherapist

Consulting Rooms (Near Lindqvist Hospital)
482 Brackenfield Road
Dunmore VIC 3987

Colin@TranquilPathway.example.au OR Marieke@TranquilPathway.example.au

Mobile: 0455 872 604 (for Colin) OR
Mobile: 0467 290 518 (for Marieke)

BACK OF CARD

Logo

Website: www.TranquilPathway.example.au

Phone: 1300 958 471

Requirements
Must have
• Text and logo only. No additiional graphics.

```html
<!DOCTYPE html>
<html lang="en">
<head>
<meta charset="utf-8">
<title>Tranquil Pathway Business Card</title>
<link href="https://fonts.googleapis.com/css2?family=Cinzel:wght@400;600&family=Tinos&family=Montserrat:wght@700&display=swap" rel="stylesheet">
<style>
  :root {
    --navy: #232c60;
    --grey: #6b6b6b;
    --ring: #6a6a6a;
    --rule: #3a3a3a;
    --paper: #ffffff;
    --border: #111111;
  }
  * { margin: 0; padding: 0; box-sizing: border-box; }
  html, body { width: 1014px; height: 1200px; overflow: hidden; background: var(--paper); }
  .sheet { position: relative; width: 1014px; height: 1200px; }
  .card {
    position: absolute; left: 30px; width: 962px; height: 562px;
    border: 3px solid var(--border); background: var(--paper);
  }
  .card--front { top: 28px; }
  .card--back { top: 616px; }
  .centered { position: absolute; left: 0; right: 0; text-align: center; white-space: nowrap; }
  .brand { position: absolute; display: flex; align-items: center; }
  .brand__dot { border-radius: 50%; background: var(--navy); border: solid var(--ring); flex: none; }
  .brand__name { font-family: "Montserrat", sans-serif; font-weight: 700; color: var(--navy); }
  .card--front .brand { left: 262px; top: 52px; gap: 28px; }
  .card--front .brand__dot { width: 136px; height: 136px; border-width: 8px; }
  .card--front .brand__name { font-size: 38px; letter-spacing: 1px; }
  .card--back .brand { left: 68px; top: 62px; gap: 60px; }
  .card--back .brand__dot { width: 268px; height: 268px; border-width: 16px; }
  .card--back .brand__name { font-size: 60px; letter-spacing: 1px; }
  .rule { position: absolute; height: 3px;
    background: linear-gradient(90deg, transparent, var(--rule) 20%, var(--rule) 80%, transparent); }
  .holder-name { top: 200px; font-family: "Cinzel", serif; font-weight: 400; font-size: 66px; color: var(--navy); letter-spacing: 2px; line-height: 1; }
  .role { top: 286px; font-family: "Cinzel", serif; font-size: 27px; color: var(--grey); letter-spacing: 1.5px; line-height: 1; }
  .address { top: 346px; font-family: "Tinos", serif; font-size: 30px; color: var(--navy); letter-spacing: 2px; line-height: 28px; }
  .contact { top: 458px; font-family: "Tinos", serif; font-size: 30px; color: var(--grey); letter-spacing: 1.5px; line-height: 28px; }
  .website { top: 420px; font-family: "Cinzel", serif; font-size: 28px; color: var(--navy); letter-spacing: 1px; line-height: 1; }
  .phone-line { top: 476px; font-family: "Cinzel", serif; font-size: 32px; color: var(--navy); letter-spacing: 2px; line-height: 1; }
  .icon { display: inline-block; vertical-align: -3px; margin-right: 8px; }
</style>
</head>
<body>
<main class="sheet">
  <section class="card card--front">
    <div class="brand">
      <span class="brand__dot"></span>
      <span class="brand__name">TRANQUIL PATHWAY</span>
    </div>
    <h1 class="centered holder-name">Colin Marchetti</h1>
    <div class="rule" style="left:46px; right:46px; top:271px;"></div>
    <p class="centered role">Professional Clinical Hypnotherapist</p>
    <p class="centered address">Consulting Rooms (Near Lindqvist Hospital)<br>482 Brackenfield Road<br>Dunmore VIC 3987</p>
    <div class="rule" style="left:110px; right:110px; top:444px;"></div>
    <p class="centered contact">Colin@TranquilPathway.example.au<br>
      <svg class="icon" width="26" height="22" viewBox="0 0 26 22" aria-hidden="true"><path fill="var(--navy)" d="M2 6c0-3 5-5 11-5s11 2 11 5v2h-6V6c-2-1-8-1-10 0v2H2zM6 9h14l4 6v6H2v-6zM13 12a3 3 0 1 0 0 6a3 3 0 0 0 0-6z"/></svg>0455 872 604</p>
  </section>

  <section class="card card--back">
    <div class="brand">
      <span class="brand__dot"></span>
      <span class="brand__name">TRANQUIL PATHWAY</span>
    </div>
    <p class="centered website">Website: www.TranquilPathway.example.au</p>
    <div class="rule" style="left:46px; right:46px; top:459px;"></div>
    <p class="centered phone-line">
      <svg class="icon" width="28" height="24" viewBox="0 0 26 22" aria-hidden="true"><path fill="var(--navy)" d="M2 6c0-3 5-5 11-5s11 2 11 5v2h-6V6c-2-1-8-1-10 0v2H2zM6 9h14l4 6v6H2v-6zM13 12a3 3 0 1 0 0 6a3 3 0 0 0 0-6z"/></svg>1300 958 471</p>
  </section>
</main>
</body>
</html>
```